Business Card Design and Stationary design for consulting firm

Harbourline Sourcing are looking for a new business card design and a design for their A4 letterhead / A4 invoices.

We are seeking to heavily increase our brand awareness and require a business card that's professional in appearance but also shows flare and innovation. A card design that people will remember.

About Us
Harbourline Sourcing are `The Sourcing Crew’.
Our mission is to be one of Australia’s greatest companies. Our aim is to help our customers achieve the best result from their purchasing experience.

Our Requirement:
• IMPACT! IMPACT! IMPACT!
• BUSINESS & PROFESSIONAL LOOKING

• Our business colours are orange, blue and green (See the logo attached).

We have provided an Art Design specification (attached) that needs to be followed for you to win the design. This also has the font, which is used on the logo.

We are after a two sided business card

Side One should have the:
The company Logo
The Sourcing Crew
www.harbourlinesourcing.com.au
Procure | Personnel | Probity & Privacy
Sydney | Melbourne | Adelaide | Brisbane

Side Two
Logo (optional)
Harbourline Sourcing (optional)
Employee details (details listed below)

The above format is our preferred option, but if you think you can come up with something better, feel free to put it forward.

We are leaving the design up to you, but it must incorporate the logo.

We will need a template that we can change the employee details on, as we will be adding more staff over the coming months.

The details below are for one employee per card with the same design.
------------------------

Employee Details:

Marcus Del Arroyo MBA, MMgmtStratProc
Principal Consultant
0491 372 618
Marcus@harbourlinesourcing.com.au

Brianna Tolley
Consulting Manager
0462 915 308
Brianna@harbourlinesourcing.com.au

Our website is www.harbourlinesourcing.com.au

The Letterhead / invoice needs to incorporate:
the company Logo
The Sourcing Crew
Sydney | Melbourne | Adelaide | Brisbane but otherwise the design is over to you.

This file needs to be delivered in word format as other detail will be added to the documents.

We look forward to you award winning designs. If you require any further information please feel free to contact us.

Regards
Harbourline Sourcing

Target Market(s)

Our Target market is companies with 80+ employees. The market we segment is heavily male based, between the ages of 35-55 years of age.

Industry/Entity Type

Consulting

Contact Information for Business Card

See Project Description

Font styles to use
Other font styles liked:
• See Art Specification

Requirements
Must have
• Company Colours, See Project Description
Should not have
• Be outside the Art specification guidelines

```html
<!DOCTYPE html>
<html lang="en">
<head>
<meta charset="utf-8">
<title>Harbourline Sourcing – Business Card</title>
<link href="https://fonts.googleapis.com/css2?family=Lato:wght@400;700&display=swap" rel="stylesheet">
<style>
  :root {
    --backdrop: #1b1b1b;
    --card: #111111;
    --card-edge: #262626;
    --map-tone: #1d2530;
    --text-main: #f2f2f2;
    --text-soft: #c9c9c9;
    --brand-orange: #f0821e;
    --brand-blue: #2f8fd6;
    --brand-green: #5cb531;
  }
  * { box-sizing: border-box; margin: 0; padding: 0; }
  html, body {
    width: 1200px; height: 873px; overflow: hidden;
    background: var(--backdrop);
    font-family: "Lato", sans-serif;
    color: var(--text-main);
  }
  .stage {
    width: 1200px; height: 873px;
    display: flex; align-items: center; justify-content: center; gap: 60px;
  }
  .card {
    position: relative;
    width: 520px; height: 318px;
    background: var(--card);
    border: 1px solid var(--card-edge);
    border-radius: 14px;
    overflow: hidden;
    box-shadow: 0 18px 40px rgba(0,0,0,.6);
  }
  .world-map {
    position: absolute;
    border-radius: 40px;
    background: radial-gradient(ellipse at center, var(--map-tone) 0%, rgba(29,37,48,0) 72%);
  }

  /* front side */
  .card--front .world-map { left: 30px; top: 40px; width: 460px; height: 240px; }
  .front-content {
    position: absolute; inset: 0;
    display: flex; flex-direction: column; align-items: center; justify-content: center;
    text-align: center;
  }
  .brand {
    display: flex; align-items: center; gap: 12px;
    font-weight: 700; font-size: 28px; color: var(--text-main);
    margin-bottom: 30px;
  }
  .brand__dot { width: 22px; height: 22px; border-radius: 50%; background: var(--text-main); }
  .services, .locations { font-size: 14px; color: var(--text-soft); line-height: 1.5; }
  .tagline {
    margin-top: 26px;
    font-size: 13px; font-weight: 700; letter-spacing: 5px;
    text-transform: uppercase; color: var(--text-soft);
  }

  /* back side */
  .card--back .world-map { left: 60px; top: 30px; width: 440px; height: 250px; }
  .back-brand {
    position: absolute; left: 32px; top: 0; bottom: 0; width: 190px;
    display: flex; flex-direction: column; align-items: center; justify-content: center; gap: 14px;
  }
  .back-brand .brand { margin: 0; font-size: 22px; flex-direction: column; gap: 12px; text-align: center; line-height: 1.15; }
  .back-brand .brand__dot { width: 30px; height: 30px; }
  .divider {
    position: absolute; left: 240px; top: 44px; width: 2px; height: 200px;
    background: linear-gradient(to bottom, rgba(255,255,255,0), #d8d8d8 50%, rgba(255,255,255,0));
  }
  .employee { position: absolute; left: 262px; top: 48px; right: 18px; }
  .employee__name { font-size: 17px; font-weight: 700; color: var(--brand-orange); }
  .employee__role { font-size: 13px; color: var(--text-main); margin-top: 3px; }
  .contact-list { list-style: none; margin-top: 40px; }
  .contact-list li {
    display: flex; align-items: center; gap: 8px;
    font-size: 13px; color: var(--text-main); margin-bottom: 9px; white-space: nowrap;
  }
  .icon {
    width: 20px; height: 20px; border-radius: 50%; flex: none;
    display: flex; align-items: center; justify-content: center;
  }
  .icon--phone { background: var(--brand-green); }
  .icon--mail { background: var(--brand-blue); }
  .icon--web { background: var(--brand-orange); }
</style>
</head>
<body>
<main class="stage">

  <section class="card card--front" aria-label="Business card front">
    <div class="world-map" role="img" aria-label="Faint dotted world map background"></div>
    <div class="front-content">
      <div class="brand"><span class="brand__dot"></span>Harbourline Sourcing</div>
      <p class="services">Procure | Personnel | Probity &amp; Privacy</p>
      <p class="locations">Sydney | Melbourne | Adelaide | Brisbane</p>
      <p class="tagline">The Sourcing Crew</p>
    </div>
  </section>

  <section class="card card--back" aria-label="Business card back">
    <div class="world-map" role="img" aria-label="Dotted world map background"></div>
    <div class="back-brand">
      <div class="brand"><span class="brand__dot"></span>Harbourline<br>Sourcing</div>
    </div>
    <div class="divider"></div>
    <div class="employee">
      <p class="employee__name">Brianna Tolley</p>
      <p class="employee__role">Consulting Manager</p>
      <ul class="contact-list">
        <li>
          <span class="icon icon--phone">
            <svg width="12" height="12" viewBox="0 0 24 24"><path fill="#fff" d="M6.6 10.8a15 15 0 0 0 6.6 6.6l2.2-2.2a1 1 0 0 1 1-.25 11.4 11.4 0 0 0 3.6.6 1 1 0 0 1 1 1V20a1 1 0 0 1-1 1A17 17 0 0 1 3 4a1 1 0 0 1 1-1h3.5a1 1 0 0 1 1 1c0 1.25.2 2.45.6 3.6a1 1 0 0 1-.25 1z"/></svg>
          </span>0462 915 308
        </li>
        <li>
          <span class="icon icon--mail">
            <svg width="12" height="12" viewBox="0 0 24 24"><rect x="2" y="5" width="20" height="14" rx="2" fill="#fff"/><path d="M3 6l9 7 9-7" fill="none" stroke="#2f8fd6" stroke-width="2"/></svg>
          </span>Brianna@harbourlinesourcing.com.au
        </li>
        <li>
          <span class="icon icon--web">
            <svg width="12" height="12" viewBox="0 0 24 24"><path d="M10 14a4 4 0 0 0 5.7 0l3-3a4 4 0 0 0-5.7-5.7l-1 1M14 10a4 4 0 0 0-5.7 0l-3 3a4 4 0 0 0 5.7 5.7l1-1" fill="none" stroke="#fff" stroke-width="2.4" stroke-linecap="round"/></svg>
          </span>www.harbourlinesourcing.com.au
        </li>
      </ul>
    </div>
  </section>

</main>
</body>
</html>
```